4' x 8' Construction Project Sign, think of a very large business card

We need project signs for our construction sites, the sign will be mounted along the road so cars driving by can quickly read. the sign should be able to be read as cars drive by doing highway speed.

Think like your making a large business card

I would like to include "NOW HIRING" Superintendents, Project Managers, Pipe Foremen, Pipe Layers, and Equipment Operators

Description of services we provide should include

Civil Construction Services
Land Clearing
Excavation
Underground Utilities
Environmental Maintenance

The 2 objectives is to market to future clients and to recruit new employees

The sign will be mounted on posts at the entrance of our construction projects
Updates

Low design quality

Target Market(s)

Construction and land developers

Industry/Entity Type

Construction Company

Other font styles liked:
• Hypatia Sans Pro lite

Colors

Designer to choose colors to be used in the design.

Requirements
Must have
• Clean and easy to read
• Civil Construction Services
• Land Clearing
• Excavation
• Underground Utilities
• Road Construction

```html
<!DOCTYPE html>
<html lang="en">
<head>
<meta charset="utf-8">
<title>Harlow Brothers – Now Hiring Project Sign</title>
<link href="https://fonts.googleapis.com/css2?family=Montserrat:wght@400;500;600;700&display=swap" rel="stylesheet">
<style>
  :root {
    --brand-blue: #213f7d;
    --panel-gray: #5f5f61;
    --sign-white: #ffffff;
    --list-text: #f1f1f1;
    --backdrop: #4b4b4b;
  }
  html, body {
    margin: 0;
    padding: 0;
    width: 1200px;
    height: 701px;
    overflow: hidden;
    background: var(--backdrop);
  }
  .project-sign {
    position: absolute;
    left: 0;
    top: 50px;
    width: 1200px;
    height: 600px;
    display: block;
  }
  .band-hiring { fill: var(--brand-blue); }
  .panel-services { fill: var(--panel-gray); }
  .panel-brand { fill: var(--sign-white); }
  .accent-triangle { fill: var(--brand-blue); }
  .headline {
    font-family: "Montserrat", sans-serif;
    font-weight: 700;
    font-size: 178px;
    fill: var(--sign-white);
  }
  .positions {
    font-family: "Montserrat", sans-serif;
    font-weight: 500;
    font-size: 35px;
    fill: var(--sign-white);
  }
  .service {
    font-family: "Montserrat", sans-serif;
    font-weight: 500;
    font-size: 31px;
    fill: var(--list-text);
  }
  .service-bullet {
    fill: none;
    stroke: var(--list-text);
    stroke-width: 2.5;
  }
  .brand-mark { fill: var(--brand-blue); }
  .brand-name {
    font-family: "Montserrat", sans-serif;
    font-weight: 600;
    font-size: 36px;
    fill: var(--brand-blue);
  }
</style>
</head>
<body>
  <svg class="project-sign" viewBox="0 0 1320 660" preserveAspectRatio="none" xmlns="http://www.w3.org/2000/svg">
    <rect class="band-hiring" x="0" y="0" width="1320" height="361"/>
    <rect class="panel-services" x="0" y="360" width="1320" height="300"/>
    <polygon class="panel-brand" points="725,360 1320,360 1320,660 682,660 630,555"/>
    <polygon class="accent-triangle" points="580,660 630,555 682,660"/>

    <text class="headline" x="93" y="197" textLength="1132">NOW HIRING</text>
    <text class="positions" x="95" y="267" textLength="1130">SUPERINTENDENTS, PROJECT MANAGERS, PIPE FOREMEN,</text>
    <text class="positions" x="95" y="315" textLength="837">PIPE LAYERS, AND EQUIPMENT OPERATORS</text>

    <g class="services-list">
      <rect class="service-bullet" x="97" y="402" width="20" height="20"/>
      <text class="service" x="133" y="422" textLength="409">Civil Construction Services</text>
      <rect class="service-bullet" x="97" y="446" width="20" height="20"/>
      <text class="service" x="133" y="466" textLength="210">Land Clearing</text>
      <rect class="service-bullet" x="97" y="495" width="20" height="20"/>
      <text class="service" x="133" y="515" textLength="167">Excavation</text>
      <rect class="service-bullet" x="97" y="538" width="20" height="20"/>
      <text class="service" x="133" y="558" textLength="330">Underground Utilities</text>
      <rect class="service-bullet" x="97" y="587" width="20" height="20"/>
      <text class="service" x="133" y="607" textLength="434">Environmental Maintenance</text>
    </g>

    <g class="brand">
      <rect class="brand-mark" x="735" y="468" width="72" height="72"/>
      <text class="brand-name" x="835" y="517" textLength="390">HARLOW BROTHERS</text>
    </g>
  </svg>
</body>
</html>
```